Brightfold

New company offering Accounting and bookkeeping for small and medium business in Cayman Islands. please see content on my website. www.brightfold.ky or www.brightfold-accountants.co.uk

Industry/Entity Type

Accounting

Requirements
Must have
• Simple, clean design
Should not have
• clutter

```html
<!DOCTYPE html>
<html lang="en">
<head>
<meta charset="utf-8">
<title>Brightfold Accountants – Flyer</title>
<link href="https://fonts.googleapis.com/css2?family=Raleway:wght@400;600;700&family=Open+Sans:wght@400;600&display=swap" rel="stylesheet">
<style>
  :root {
    --brand-blue: #2b4f9e;
    --sky-blue: #3d8fd6;
    --brand-green: #3aa757;
    --ink: #4a4f57;
    --rule: #c9d3e0;
    --paper: #ffffff;
    --photo-light: #e9edf1;
    --photo-dark: #b9c0c8;
  }
  * { box-sizing: border-box; margin: 0; padding: 0; }
  html, body { width: 802px; height: 1200px; overflow: hidden; background: var(--paper); }
  .flyer { position: relative; width: 802px; height: 1200px; background: var(--paper); font-family: "Open Sans", sans-serif; color: var(--ink); }

  .flyer__header { position: absolute; left: 0; top: 0; width: 802px; height: 560px; }

  .brand { position: absolute; left: 48px; top: 52px; display: flex; align-items: center; gap: 14px; }
  .brand__dot { width: 52px; height: 52px; border-radius: 50%; background: var(--brand-green); }
  .brand__name { font-family: "Raleway", sans-serif; font-weight: 700; font-size: 30px; letter-spacing: 1px; color: var(--brand-blue); text-transform: uppercase; line-height: 1; }

  .headline { position: absolute; left: 120px; right: 48px; top: 560px; text-align: right; font-family: "Raleway", sans-serif; font-weight: 400; text-transform: uppercase; color: var(--sky-blue); }
  .headline__name { display: block; font-size: 40px; font-weight: 600; letter-spacing: 1px; }
  .headline__tag { display: block; font-size: 30px; letter-spacing: 1px; margin-top: 4px; }

  .section-title { display: flex; align-items: center; gap: 16px; font-family: "Raleway", sans-serif; font-weight: 600; font-size: 26px; color: var(--brand-green); text-transform: uppercase; letter-spacing: 1px; }
  .section-title::before, .section-title::after { content: ""; flex: 1; height: 2px; background: var(--rule); }

  .about { position: absolute; left: 60px; right: 60px; top: 680px; }
  .about__text { margin-top: 16px; font-size: 15px; line-height: 1.65; text-align: center; }

  .services { position: absolute; left: 60px; right: 60px; top: 885px; }
  .services__list { list-style: none; display: flex; justify-content: space-between; margin-top: 26px; padding: 0 10px; }
  .service { display: flex; align-items: center; gap: 12px; font-size: 15px; width: 165px; }
  .service__icon { flex: none; width: 48px; height: 48px; background: var(--brand-green); }

  .flyer__footer { position: absolute; left: 0; bottom: 0; width: 802px; height: 120px; }
  .footer__address { position: absolute; left: 60px; bottom: 64px; font-size: 13px; color: var(--ink); }
</style>
</head>
<body>
<main class="flyer">
  <svg class="flyer__header" viewBox="0 0 802 560" aria-hidden="false">
    <polygon points="0,250 802,110 802,90 0,230" fill="var(--brand-blue)"/>
    <polygon points="0,262 802,122 802,114 0,254" fill="var(--brand-green)"/>
    <defs>
      <linearGradient id="photoTone" x1="0" y1="0" x2="1" y2="1">
        <stop offset="0" stop-color="var(--photo-light)"/>
        <stop offset="1" stop-color="var(--photo-dark)"/>
      </linearGradient>
    </defs>
    <polygon role="img" aria-label="Photo of business people reviewing financial documents with pens at a desk" points="0,268 802,128 802,430 0,500" fill="url(#photoTone)"/>
    <polygon points="0,500 802,430 802,446 0,516" fill="var(--brand-blue)"/>
    <polygon points="0,522 802,452 802,458 0,528" fill="var(--brand-green)"/>
  </svg>

  <div class="brand">
    <span class="brand__dot"></span>
    <span class="brand__name">Brightfold</span>
  </div>

  <h1 class="headline">
    <span class="headline__name">Brightfold Accountants:</span>
    <span class="headline__tag">Your partner for successful growth</span>
  </h1>

  <section class="about">
    <h2 class="section-title">About us</h2>
    <p class="about__text">Originating in London, Brightfold brings years of accounting practice to the Cayman Islands. Our team are qualified, friendly and experienced members of recognised professional bodies, and we are proud to support small and medium businesses with clear, timely and affordable services. Whatever your sector, we offer a wide range of solutions tailored to your commercial and personal needs.</p>
  </section>

  <section class="services">
    <h2 class="section-title">Our services</h2>
    <ul class="services__list">
      <li class="service">
        <svg class="service__icon" viewBox="0 0 48 48"><rect width="48" height="48" fill="var(--brand-green)"/><rect x="14" y="12" width="20" height="24" fill="none" stroke="#fff" stroke-width="2.5"/><line x1="18" y1="19" x2="30" y2="19" stroke="#fff" stroke-width="2"/><line x1="18" y1="25" x2="30" y2="25" stroke="#fff" stroke-width="2"/><line x1="18" y1="31" x2="26" y2="31" stroke="#fff" stroke-width="2"/></svg>
        <span>Bookkeeping</span>
      </li>
      <li class="service">
        <svg class="service__icon" viewBox="0 0 48 48"><rect width="48" height="48" fill="var(--brand-green)"/><rect x="13" y="26" width="5" height="10" fill="#fff"/><rect x="21" y="20" width="5" height="16" fill="#fff"/><rect x="29" y="13" width="5" height="23" fill="#fff"/></svg>
        <span>Management Accounts</span>
      </li>
      <li class="service">
        <svg class="service__icon" viewBox="0 0 48 48"><rect width="48" height="48" fill="var(--brand-green)"/><rect x="12" y="16" width="24" height="16" fill="none" stroke="#fff" stroke-width="2.5"/><circle cx="24" cy="24" r="4" fill="#fff"/></svg>
        <span>Payroll</span>
      </li>
      <li class="service">
        <svg class="service__icon" viewBox="0 0 48 48"><rect width="48" height="48" fill="var(--brand-green)"/><circle cx="24" cy="24" r="9" fill="none" stroke="#fff" stroke-width="2.5"/><polyline points="19,24 23,28 30,20" fill="none" stroke="#fff" stroke-width="2.5"/></svg>
        <span>Other Services</span>
      </li>
    </ul>
  </section>

  <p class="footer__address">PO Box 4410, Harbour Lane, Grand Cayman KY1-1207</p>
  <svg class="flyer__footer" viewBox="0 0 802 120" aria-hidden="true">
    <polygon points="0,80 802,40 802,48 0,88" fill="var(--brand-green)"/>
    <polygon points="0,94 802,54 802,120 0,120" fill="var(--brand-blue)"/>
  </svg>
</main>
</body>
</html>
```